Oral Surgery Office Referral Form and Stationary designs.

Hi, I am a dentist/oral surgeon recently graduated and starting my own practice. Need help in designing an attractive, warm, appealing and Professional referral form (double sided), and stationary design. These will be used for Thank you notes, Professional letters, Front of a presentation folder, Notepads, envelopes, promotional products, Fax, etc... I do have a sample of a typical referral form and also have a logo as well as business card design that I will provide as a base to use. I will attach the files to this posting. Please, do some investigating on the Oral surgery / dental specialist websites as to some of the examples of the referral forms. Thanks and feel free to respond with any questions. Look forward to the designs - having the business card designed here was a great experience.
I will attach more files to clarify / show examples.

HELLO ALL,

I JUST WENT THROUGH THE BRIEF AND REALISED THAT THERE IS A MISTAKE IN MY POSTING. 
THE WEBSITE ADDRESS SHOULD READ:
 WWW.KTRDX.COM 
IN MY ORIGINAL POSTING IT WAS MISSING THE "M".

TRULY APOLOGIZE FOR ANY INCONVENIENCE.
THANK YOU,
GERALD

Target Market(s)

Dental Professionals and oral surgery patients.

Industry/Entity Type

Dental

Requirements
Must have
• Has to have pictures of the mouth / teeth numbers/ map with directions. Needs to be warm and appealing. If possible to have it in a format that can be easily converted to a clickable one online. Don't know if possible. Thanks.
Should not have
• Typical dental designs .

```html
<!DOCTYPE html>
<html lang="en">
<head>
<meta charset="utf-8">
<title>Willow Crest Oral Surgery – Referral Form</title>
<link href="https://fonts.googleapis.com/css2?family=Lato:wght@400;700&family=Arimo:wght@400;700&display=swap" rel="stylesheet">
<style>
  :root{
    --brand-blue:#0a6fa8;
    --text-blue:#1a7bb8;
    --tint-blue:#d6e8f4;
    --pale-blue:#eef5fa;
    --map-blue:#a9cde8;
    --ink:#1c1c1c;
    --paper:#ffffff;
  }
  html,body{margin:0;padding:0;width:1200px;height:900px;overflow:hidden;background:var(--paper);}
  svg.sheet{display:block;width:1200px;height:900px;}
  .panel-frame{fill:var(--paper);stroke:var(--brand-blue);stroke-width:3;}
  .rule{stroke:var(--brand-blue);stroke-width:1;}
  .label{font-family:"Lato",sans-serif;font-size:8.5px;fill:var(--ink);letter-spacing:.4px;}
  .note{font-family:"Lato",sans-serif;font-size:8px;fill:var(--text-blue);letter-spacing:.2px;}
  .heading{font-family:"Lato",sans-serif;font-size:9px;fill:var(--ink);letter-spacing:.4px;}
  .option{font-family:"Lato",sans-serif;font-size:7.5px;fill:var(--text-blue);letter-spacing:.2px;}
  .tooth-num{font-family:"Lato",sans-serif;font-size:8px;fill:var(--text-blue);text-anchor:middle;}
  .check{fill:none;stroke:var(--brand-blue);stroke-width:1;}
  .grid{fill:none;stroke:var(--brand-blue);stroke-width:.8;}
  .tooth-area{fill:var(--tint-blue);}
  .brand-mark{fill:var(--brand-blue);}
  .brand-name{font-family:"Lato",sans-serif;font-size:15px;fill:var(--brand-blue);text-anchor:middle;letter-spacing:.5px;}
  .brand-name.small{font-size:11px;}
  .flip{font-family:"Lato",sans-serif;font-size:8px;fill:var(--text-blue);text-anchor:middle;}
  .doctor{font-family:"Arimo",sans-serif;font-size:10px;fill:var(--text-blue);text-anchor:middle;}
  .contact{font-family:"Arimo",sans-serif;font-size:10px;fill:var(--text-blue);text-anchor:middle;}
  .address{font-family:"Arimo",sans-serif;font-size:10.5px;fill:var(--ink);text-anchor:middle;}
  .notice{font-family:"Arimo",sans-serif;font-size:8.6px;fill:var(--ink);}
  .instruction{font-family:"Arimo",sans-serif;font-size:8.2px;fill:var(--text-blue);}
  .map-area{fill:var(--map-blue);}
  .divider-band{fill:var(--brand-blue);}
  .backdrop-wave{fill:var(--pale-blue);}
  .phone-icon{fill:var(--ink);}
</style>
</head>
<body>
<svg class="sheet" viewBox="0 0 1200 900" xmlns="http://www.w3.org/2000/svg">

  <!-- ===== Front panel: referral form ===== -->
  <g class="front-panel">
    <rect class="panel-frame" x="54" y="195" width="528" height="528"/>
    <path class="backdrop-wave" d="M56 380 C200 330 380 420 580 360 L580 420 C380 470 200 390 56 430 Z"/>

    <text class="note" x="569" y="209" text-anchor="end">save time! : fill out patient registration &amp; health history online.</text>

    <text class="label" x="68" y="230">TODAY'S DATE</text>
    <path class="phone-icon" d="M298 226 c2 -6 16 -6 18 0 l-1 2.5 h-4 l-.6 -2 h-6.8 l-.6 2 h-4 z"/>
    <text class="label" x="329" y="230">#</text>
    <line class="rule" x1="66" y1="233" x2="570" y2="233"/>

    <text class="label" x="68" y="262">NAME</text>
    <text class="label" x="294" y="262">REFERRED BY</text>
    <line class="rule" x1="66" y1="265" x2="570" y2="265"/>

    <text class="label" x="68" y="293">ADDITIONAL COMMENTS</text>
    <line class="rule" x1="66" y1="296" x2="570" y2="296"/>
    <line class="rule" x1="66" y1="327" x2="570" y2="327"/>

    <text class="note" x="318" y="349" text-anchor="middle">Appointment Information : This time is reserved specifically for you. If by necessity, you must cancel your appointment for</text>
    <text class="note" x="318" y="361" text-anchor="middle">surgery please notify us at least one day / 24 hours in advance.</text>

    <circle class="check" cx="315" cy="381" r="9"/>
    <circle class="check" cx="336" cy="381" r="9"/>
    <circle class="check" cx="457" cy="381" r="9"/>
    <circle class="check" cx="477" cy="381" r="9"/>
    <circle class="check" cx="497" cy="381" r="9"/>
    <circle class="check" cx="516" cy="381" r="9"/>
    <circle class="check" cx="536" cy="381" r="9"/>
    <circle class="check" cx="556" cy="381" r="9"/>

    <text class="label" x="69" y="404">APPT DATE</text>
    <text class="label" x="211" y="404">TIME</text>
    <text class="label" x="260" y="404">:</text>
    <text class="label" x="307" y="404">AM&#160;&#160;PM</text>
    <text class="label" x="420" y="404">DAY</text>
    <text class="label" x="453" y="404">M&#160;&#160;&#160;&#160;T&#160;&#160;&#160;&#160;W&#160;&#160;&#160;TH&#160;&#160;&#160;F&#160;&#160;&#160;&#160;S</text>
    <line class="rule" x1="66" y1="407" x2="570" y2="407"/>

    <text class="note" x="318" y="419" text-anchor="middle">Please check off areas to be examined during consultation :</text>

    <!-- permanent teeth chart -->
    <g class="permanent-chart">
      <rect class="grid" x="63" y="430" width="282" height="8"/>
      <rect class="grid" x="63" y="523" width="282" height="8"/>
      <path class="grid" d="M80.6 430v8M98.3 430v8M115.9 430v8M133.5 430v8M151.1 430v8M168.8 430v8M186.4 430v8M204 430v8M221.6 430v8M239.3 430v8M256.9 430v8M274.5 430v8M292.1 430v8M309.8 430v8M327.4 430v8
                            M80.6 523v8M98.3 523v8M115.9 523v8M133.5 523v8M151.1 523v8M168.8 523v8M186.4 523v8M204 523v8M221.6 523v8M239.3 523v8M256.9 523v8M274.5 523v8M292.1 523v8M309.8 523v8M327.4 523v8"/>
      <path class="grid" d="M151 438v85M204 438v85M257 438v85"/>
      <rect class="tooth-area" x="64" y="441" width="280" height="28" role="img" aria-label="Upper adult teeth diagram, numbered 1 to 16"/>
      <rect class="tooth-area" x="64" y="496" width="280" height="25" role="img" aria-label="Lower adult teeth diagram, numbered 17 to 32"/>
      <text class="tooth-num" y="480">
        <tspan x="72">16</tspan><tspan x="89">15</tspan><tspan x="107">14</tspan><tspan x="125">13</tspan><tspan x="142">12</tspan><tspan x="160">11</tspan><tspan x="178">10</tspan><tspan x="195">9</tspan><tspan x="213">8</tspan><tspan x="230">7</tspan><tspan x="248">6</tspan><tspan x="266">5</tspan><tspan x="283">4</tspan><tspan x="301">3</tspan><tspan x="319">2</tspan><tspan x="336">1</tspan>
      </text>
      <text class="tooth-num" y="493">
        <tspan x="72">17</tspan><tspan x="89">18</tspan><tspan x="107">19</tspan><tspan x="125">20</tspan><tspan x="142">21</tspan><tspan x="160">22</tspan><tspan x="178">23</tspan><tspan x="195">24</tspan><tspan x="213">25</tspan><tspan x="230">26</tspan><tspan x="248">27</tspan><tspan x="266">28</tspan><tspan x="283">29</tspan><tspan x="301">30</tspan><tspan x="319">31</tspan><tspan x="336">32</tspan>
      </text>
    </g>

    <!-- primary teeth chart -->
    <g class="primary-chart">
      <rect class="grid" x="453" y="430" width="112" height="8"/>
      <rect class="grid" x="453" y="523" width="112" height="8"/>
      <path class="grid" d="M464.2 430v8M475.4 430v8M486.6 430v8M497.8 430v8M509 430v8M520.2 430v8M531.4 430v8M542.6 430v8M553.8 430v8
                            M464.2 523v8M475.4 523v8M486.6 523v8M497.8 523v8M509 523v8M520.2 523v8M531.4 523v8M542.6 523v8M553.8 523v8"/>
      <rect class="tooth-area" x="454" y="446" width="110" height="24" role="img" aria-label="Upper primary teeth diagram, lettered A to J"/>
      <rect class="tooth-area" x="454" y="496" width="110" height="25" role="img" aria-label="Lower primary teeth diagram, lettered K to T"/>
      <text class="tooth-num" y="480" x="458.6 469.8 481 492.2 503.4 514.6 525.8 537 548.2 559.4">ABCDEFGHIJ</text>
      <text class="tooth-num" y="492" x="458.6 469.8 481 492.2 503.4 514.6 525.8 537 548.2 559.4">KLMNOPQRST</text>
    </g>

    <text class="heading" x="194" y="550" text-anchor="middle">REASON FOR CONSULTATION</text>
    <text class="heading" x="362" y="550" text-anchor="middle">SURGICAL TEMPLATE</text>
    <text class="heading" x="519" y="550" text-anchor="middle">RADIOGRAPHS</text>

    <!-- reasons column 1 -->
    <g class="reason-list">
      <circle class="check" cx="82" cy="564" r="6"/><text class="option" x="94" y="567">Wisdom Teeth</text>
      <circle class="check" cx="82" cy="580" r="6"/><text class="option" x="94" y="583">Extraction</text>
      <circle class="check" cx="82" cy="596" r="6"/><text class="option" x="94" y="599">Implants</text>
      <circle class="check" cx="82" cy="612" r="6"/><text class="option" x="94" y="615">Bone Grafting</text>
      <circle class="check" cx="82" cy="628" r="6"/><text class="option" x="94" y="631">Exposure &amp; Bonding</text>
      <circle class="check" cx="82" cy="644" r="6"/><text class="option" x="94" y="647">Biopsy</text>
      <circle class="check" cx="82" cy="660" r="6"/><text class="option" x="94" y="663">Lesion Evaluation</text>
      <circle class="check" cx="82" cy="676" r="6"/><text class="option" x="94" y="679">Infection (I&amp;D)</text>
      <circle class="check" cx="82" cy="692" r="6"/><text class="option" x="94" y="695">Alveoloplasty</text>
      <circle class="check" cx="82" cy="708" r="6"/><text class="option" x="94" y="711">Frenectomy</text>
    </g>

    <!-- reasons column 2 -->
    <g class="reason-list">
      <circle class="check" cx="186" cy="564" r="6"/><text class="option" x="197" y="567">TMJ</text>
      <circle class="check" cx="186" cy="580" r="6"/><text class="option" x="197" y="583">Implants</text>
      <circle class="check" cx="207" cy="596" r="5.5"/><text class="option" x="216" y="599">Kelvra</text>
      <circle class="check" cx="207" cy="612" r="5.5"/><text class="option" x="216" y="615">Odunix</text>
      <circle class="check" cx="207" cy="628" r="5.5"/><text class="option" x="216" y="631">Pellam</text>
      <circle class="check" cx="207" cy="644" r="5.5"/><text class="option" x="216" y="647">Q7</text>
      <circle class="check" cx="207" cy="660" r="5.5"/><text class="option" x="216" y="663">Other_________</text>
      <circle class="check" cx="186" cy="676" r="6"/><text class="option" x="197" y="679">Consultation</text>
      <circle class="check" cx="186" cy="692" r="6"/><text class="option" x="197" y="695">Radiographs</text>
      <circle class="check" cx="186" cy="708" r="6"/><text class="option" x="197" y="711">Other_____________</text>
    </g>

    <!-- surgical template -->
    <g class="template-list">
      <circle class="check" cx="282" cy="563" r="6"/><text class="option" x="291" y="566">To be provided by restorative dentist</text>
      <circle class="check" cx="282" cy="580" r="6"/><text class="option" x="291" y="583">To be fabricated by the surgeon</text>
      <circle class="check" cx="282" cy="598" r="6"/><text class="option" x="291" y="601">Other ___________________________</text>
    </g>

    <!-- radiographs -->
    <g class="radiograph-list">
      <circle class="check" cx="470" cy="561" r="6"/><text class="option" x="480" y="564">Being Mailed/Emailed,</text>
      <circle class="check" cx="470" cy="579" r="6"/><text class="option" x="480" y="582">Given to the Patient,</text>
      <circle class="check" cx="470" cy="597" r="6"/><text class="option" x="480" y="600">Please Take.</text>
      <circle class="check" cx="470" cy="614" r="6"/><text class="option" x="480" y="617">Other_____________</text>
      <line class="rule" x1="480" y1="635" x2="557" y2="635"/>
    </g>

    <!-- practice name -->
    <rect class="brand-mark" x="404" y="626" width="34" height="34"/>
    <text class="brand-name" x="421" y="692">Willow Crest</text>
    <text class="brand-name" x="421" y="710">ORAL SURGERY</text>

    <text class="flip" x="539" y="663">flip form</text>
    <text class="flip" x="539" y="673">for more</text>
    <path d="M521 686 H560 M553 681 L561 686 L553 691" fill="none" stroke="var(--brand-blue)" stroke-width="1.6"/>
  </g>

  <!-- ===== Back panel: practice info & instructions ===== -->
  <g class="back-panel">
    <rect class="panel-frame" x="590" y="195" width="527" height="528"/>

    <rect class="brand-mark" x="723" y="215" width="33" height="33"/>
    <text class="brand-name small" x="740" y="265">Willow Crest</text>
    <text class="brand-name small" x="740" y="278">ORAL SURGERY</text>

    <text class="doctor" x="743" y="317">GERALD I. HALVORSEN DDS, MD</text>
    <text class="doctor" x="743" y="327">DIPLOMATE, NORTHLAKE COUNCIL OF</text>
    <text class="doctor" x="743" y="337">ORAL &amp; FACIAL SURGERY</text>

    <text class="contact" x="741" y="353">www.ktrdx.com</text>
    <text class="contact" x="741" y="363">phone: 402.555.0148</text>
    <text class="contact" x="741" y="373">fax. 402.555.0149</text>

    <text class="address" x="744" y="388">4810 Alder Street</text>
    <text class="address" x="744" y="399">Lindenfield, NE 68100</text>

    <rect class="map-area" x="873" y="213" width="183" height="178" role="img" aria-label="Street map showing directions to the practice"/>

    <!-- plain divider band -->
    <rect class="divider-band" x="592" y="424" width="523" height="10"/>

    <text class="notice" x="611" y="473">PLEASE NOTE THAT IN MOST INSTANCES THE PATIENT IS FIRST SEEN FOR CONSULATION TO REVIEW THE</text>
    <text class="notice" x="611" y="482">HEALTH HISTORY; DECIDE ON THE MOST APPROPRIATE ANESTHESIA AND TREATMENT PLAN, AND</text>
    <text class="notice" x="611" y="491">SCHEDULE THE SURGERY AT A SEPARATE APPOINTMENT.</text>

    <text class="instruction" x="633" y="509">Please assist us by having the following information available with you at the time of appointment:</text>
    <text class="instruction" x="633" y="527">Your surgical referral slip and any x-rays if applicable, a list of medications, and insurance policy information.</text>
    <text class="instruction" x="633" y="545">IMPORTANT: All patients unmarried or under the age of 19 must be accompanied by a Parent or guardian during the</text>
    <text class="instruction" x="633" y="554">Consultation and Treatment visits.</text>

    <text class="notice" x="611" y="580">SPECIAL INSTRUCTIONS FOR PATIENTS HAVING I.V. SEDATION / GENERAL ANESTHESIA:</text>

    <text class="instruction" x="633" y="597">NO FOOD OR DRINK (including WATER) AT LEAST 6 HOURS PRIOR TO YOUR SURGERY UNLESS</text>
    <text class="instruction" x="633" y="606">OTHERWISE INDICATED BY THE SURGEON.</text>
    <text class="instruction" x="633" y="623">Some medicaitons may be continued and this will be discussed at your consultation</text>
    <text class="instruction" x="633" y="640">A responsible adult must accompany you and REMAIN in the office during the entire treatment. They must also be</text>
    <text class="instruction" x="633" y="649">able to drive you home. YOU cannot drive until the next day.</text>
    <text class="instruction" x="633" y="667">Eat a light and easily digestible meal the night before the procedure. Do not drink any alcoholic beverages the night</text>
    <text class="instruction" x="633" y="676">before.</text>
    <text class="instruction" x="633" y="694">Wear comfortable clothing with sleeves which are easy to push up.</text>
  </g>
</svg>
</body>
</html>
```